Structural Engineering Business Card

Veltrow Drafts does residential house plans for clients in Central Florida. Would like simple but elegant business card that is appropriate for a house plan engineering company. Prefer black business card with black/white them but open to other shades of blue. I uploaded a sample card that I came across that looked good but please come up with your own creative designs.

Contact Information for Business Card

Name, Title, Phone, Email, Address, website

```html
<!DOCTYPE html>
<html lang="en">
<head>
<meta charset="utf-8">
<title>Veltrow Drafts — Business Card</title>
<link href="https://fonts.googleapis.com/css2?family=Open+Sans:wght@400;700;800&display=swap" rel="stylesheet">
<style>
  :root {
    --backdrop: #3a3b3d;
    --card: #020203;
    --edge: #6cc3e8;
    --accent: #4fb0dd;
    --ink: #ffffff;
    --ink-soft: #e6e6e6;
    --grid-tone: #1a1a1c;
  }
  * { margin: 0; padding: 0; box-sizing: border-box; }
  html, body { width: 1200px; height: 900px; overflow: hidden; }
  body {
    background: var(--backdrop);
    font-family: "Open Sans", Arial, sans-serif;
    position: relative;
  }
  .card {
    position: absolute;
    left: 250px;
    width: 700px;
    height: 400px;
    background: var(--card);
    border: 9px solid var(--edge);
    overflow: hidden;
    box-shadow: 0 10px 24px rgba(0,0,0,.45);
  }
  .card--back { top: 33px; }
  .card--front { top: 467px; }

  .grid-corner {
    position: absolute;
    top: 0; bottom: 0;
    width: 230px;
  }
  .grid-corner--left { left: 0; background: linear-gradient(100deg, var(--grid-tone) 0%, var(--card) 70%); }
  .grid-corner--right { right: 0; background: linear-gradient(260deg, var(--grid-tone) 0%, var(--card) 70%); }

  .wordmark {
    position: absolute;
    color: var(--ink);
    font-weight: 800;
    letter-spacing: 0.5px;
    white-space: nowrap;
  }
  .card--back .wordmark {
    top: 130px; left: 0; right: 0;
    text-align: center;
    font-size: 46px;
  }
  .back-rule {
    position: absolute;
    top: 212px; left: 175px; right: 175px;
    height: 1px;
    background: var(--accent);
  }
  .site-spaced {
    position: absolute;
    top: 228px; left: 0; right: 0;
    text-align: center;
    color: var(--ink-soft);
    font-size: 15px;
    letter-spacing: 9px;
  }

  .card--front .wordmark { top: 78px; right: 60px; font-size: 42px; }

  .person { position: absolute; left: 60px; right: 60px; top: 218px; }
  .person__row { display: flex; align-items: flex-end; }
  .person__name {
    color: var(--accent);
    font-weight: 700;
    font-size: 20px;
    letter-spacing: .5px;
    line-height: 1.1;
    white-space: nowrap;
  }
  .person__rule {
    flex: 1;
    height: 1px;
    margin: 0 0 4px 8px;
    background: var(--accent);
  }
  .person__title { color: var(--ink-soft); font-size: 16px; margin-top: 4px; }

  .contact { position: absolute; list-style: none; color: var(--ink-soft); font-size: 16px; }
  .contact li { display: flex; align-items: center; gap: 8px; height: 26px; white-space: nowrap; }
  .contact svg { width: 15px; height: 15px; fill: var(--accent); flex: none; }
  .contact--left { left: 60px; top: 298px; }
  .contact--right { right: 60px; top: 266px; }
</style>
</head>
<body>

<section class="card card--back" aria-label="Card back">
  <div class="grid-corner grid-corner--left" role="img" aria-label="Faint architectural grid lines"></div>
  <div class="grid-corner grid-corner--right" role="img" aria-label="Faint architectural grid lines"></div>
  <div class="wordmark">Veltrow Drafts</div>
  <div class="back-rule"></div>
  <div class="site-spaced">www.veltrowdrafts.com</div>
</section>

<section class="card card--front" aria-label="Card front">
  <div class="grid-corner grid-corner--left" role="img" aria-label="Faint architectural grid lines"></div>
  <div class="grid-corner grid-corner--right" role="img" aria-label="Faint architectural grid lines"></div>
  <div class="wordmark">Veltrow Drafts</div>

  <div class="person">
    <div class="person__row">
      <div class="person__name">AREN HOLLOWAY</div>
      <div class="person__rule"></div>
    </div>
    <div class="person__title">Architectural Director</div>
  </div>

  <ul class="contact contact--left">
    <li>
      <svg viewBox="0 0 24 24" aria-hidden="true"><path d="M6.6 10.8a15.2 15.2 0 0 0 6.6 6.6l2.2-2.2a1 1 0 0 1 1-.25 11.4 11.4 0 0 0 3.6.57 1 1 0 0 1 1 1V20a1 1 0 0 1-1 1A17 17 0 0 1 3 4a1 1 0 0 1 1-1h3.5a1 1 0 0 1 1 1c0 1.25.2 2.45.57 3.6a1 1 0 0 1-.25 1z"/></svg>
      555-214-7730
    </li>
    <li>
      <svg viewBox="0 0 24 24" aria-hidden="true"><path d="M12 2a7 7 0 0 0-7 7c0 5.2 7 13 7 13s7-7.8 7-13a7 7 0 0 0-7-7zm0 9.5A2.5 2.5 0 1 1 12 6.5a2.5 2.5 0 0 1 0 5z"/></svg>
      99 dummy city, dummy 0000
    </li>
  </ul>

  <ul class="contact contact--right">
    <li>
      <svg viewBox="0 0 24 24" aria-hidden="true"><path d="M3 5h18a1 1 0 0 1 1 1v12a1 1 0 0 1-1 1H3a1 1 0 0 1-1-1V6a1 1 0 0 1 1-1zm9 7.5L20 7H4z"/></svg>
      info@veltrowdrafts.com
    </li>
    <li>
      <svg viewBox="0 0 24 24" aria-hidden="true"><path d="M12 2a10 10 0 1 0 0 20 10 10 0 0 0 0-20zm6.9 9h-3a15 15 0 0 0-1.3-5.6A8 8 0 0 1 18.9 11zM12 4.1c.9 1.2 1.8 3.6 1.9 6.9h-3.8c.1-3.3 1-5.7 1.9-6.9zM9.4 5.4A15 15 0 0 0 8.1 11h-3a8 8 0 0 1 4.3-5.6zM5.1 13h3a15 15 0 0 0 1.3 5.6A8 8 0 0 1 5.1 13zm6.9 6.9c-.9-1.2-1.8-3.6-1.9-6.9h3.8c-.1 3.3-1 5.7-1.9 6.9zm2.6-1.3a15 15 0 0 0 1.3-5.6h3a8 8 0 0 1-4.3 5.6z"/></svg>
      www.veltrowdrafts.com
    </li>
  </ul>
</section>

</body>
</html>
```